New website for an SEO training system

We need a web design for an SEO company offering a Pagewick Method product which is a system or recipe on how to do SEO on your blog. It's a bit like, "Forty Evenings Toward a Sharper Journal" in that they it is chunked down to what should be done on a daily basis over a 30 day period. It's not so much a training product but a recipe book.
The materials are video and support docs, like to do lists and checklists. It needs to be fresh and clean, with modern design.

Target Market(s)

Bloggers

Industry/Entity Type

It Company

Font styles to use
Sans Serif

```html
<!DOCTYPE html>
<html lang="en">
<head>
<meta charset="utf-8">
<title>Pagewick Method</title>
<link rel="stylesheet" href="https://fonts.googleapis.com/css2?family=Lato:wght@300;400;700&display=swap">
<style>
:root{
  --orange:#f7823a;
  --ink:#1f1f1f;
  --text:#333;
  --muted:#555;
  --hero-bg:#f4f4f4;
  --dark:#2e2f34;
  --footer:#464646;
  --white:#fff;
  --icon-blue:#1f4f8a;
  --icon-amber:#f7a324;
}
*{box-sizing:border-box;margin:0;padding:0}
html,body{width:877px;height:1200px;overflow:hidden}
body{font-family:'Lato',sans-serif;color:var(--text);background:var(--white);position:relative}
.page{position:relative;width:877px;height:1200px;overflow:hidden}
section,header,footer{position:absolute;left:0;width:877px}

/* header */
.site-header{top:0;height:64px;background:#fbfbfb;border-bottom:1px solid #ddd;box-shadow:0 2px 4px rgba(0,0,0,.12);z-index:2}
.brand{position:absolute;left:124px;top:16px;display:flex;align-items:center;gap:10px;font-size:19px;font-weight:400;color:#555;letter-spacing:.5px}
.brand-dot{width:22px;height:22px;border-radius:50%;background:#2b2b2b}
.main-nav{position:absolute;top:39px;left:392px;font-size:10px;color:#222;text-transform:uppercase}
.main-nav span{position:absolute;white-space:nowrap}
.social{position:absolute;top:12px;left:687px;display:flex;gap:6px}
.social i{display:block;width:17px;height:17px;border-radius:50%;background:#444}

/* hero */
.hero{top:64px;height:348px;background:var(--hero-bg)}
.hero h1{position:absolute;top:28px;left:0;width:804px;text-align:center;font-weight:400;font-size:31px;color:var(--ink)}
.hero .lead{position:absolute;top:69px;left:0;width:818px;text-align:center;font-size:11.5px;color:#222}
.hero-visual{position:absolute;left:106px;top:116px;width:302px;height:170px;border-radius:6px 6px 3px 3px;background:linear-gradient(160deg,#e9e9e9 0%,#f1f1f1 45%,#f26b1d 75%,#2a2a2a 100%)}
.feature-list{position:absolute;left:451px;top:103px;list-style:none}
.feature-list li{display:flex;align-items:center;gap:13px;height:31.5px;font-size:11.5px;font-weight:700;color:#222}
.feature-list svg{width:19px;height:19px}
.cta-button{position:absolute;left:455px;top:252px;width:219px;height:67px;border-radius:4px;background:var(--orange);color:var(--white);font-weight:700;font-size:19px;line-height:23px;text-align:center;padding-top:10px}

/* stories */
.stories{top:412px;height:165px;background:var(--dark)}
.story{position:absolute;top:26px;display:flex}
.story-video{width:146px;height:105px;border:6px solid var(--white);border-radius:5px;background:linear-gradient(135deg,#1c1c1c,#4a4a4a 60%,#222)}
.story-video.alt{width:148px;background:linear-gradient(135deg,#7a747a,#a19aa6 55%,#5c4e6a)}
.story h3{font-size:12.5px;font-weight:700;color:var(--white);margin:2px 0 8px}
.story p{font-size:11px;line-height:13.5px;color:#ddd;width:112px}

/* create band */
.create-band{top:577px;height:102px;background:var(--orange);text-align:center;color:var(--white)}
.create-band h2{font-weight:300;font-size:36px;margin-top:15px}
.create-band p{font-size:14px;margin-top:3px}

/* capabilities */
.capabilities{top:679px;height:216px;background:var(--white)}
.capability{position:absolute;display:flex;align-items:center;gap:8px}
.capability h4{font-size:16px;font-weight:400;color:var(--ink);margin-bottom:5px}
.capability p{font-size:9px;color:var(--muted)}
.cap-icon{width:43px;height:43px;border-radius:10px;flex:none}
.cap-icon.blue{background:var(--icon-blue)}
.cap-icon.amber{background:var(--icon-amber)}

/* guarantee */
.guarantee{top:895px;height:183px;background:#f3f3f3}
.guarantee-badge{position:absolute;left:148px;top:24px;width:124px;height:124px;border-radius:50%;background:#1d1d1d}
.guarantee-badge::after{content:"";position:absolute;left:28px;top:28px;width:68px;height:68px;border-radius:50%;background:#7cc62a}
.guarantee h3{position:absolute;left:303px;top:38px;font-size:18px;font-weight:400;color:var(--ink)}
.guarantee p{position:absolute;left:307px;top:66px;width:492px;font-size:8.6px;line-height:10.8px;color:#444}

/* questions */
.questions{top:1078px;height:59px;background:var(--orange);display:flex;align-items:center;justify-content:center;gap:8px;padding-left:40px}
.questions h3{font-size:21px;font-weight:700;color:var(--ink)}

/* footer */
.site-footer{top:1137px;height:63px;background:var(--footer);color:var(--white);font-size:9.5px;font-weight:700}
.site-footer .copy{position:absolute;left:140px;top:37px}
.site-footer .legal{position:absolute;left:618px;top:33px;display:flex;gap:20px}
</style>
</head>
<body>
<div class="page">

<header class="site-header">
  <div class="brand"><span class="brand-dot"></span>PAGEWICK METHOD</div>
  <nav class="main-nav">
    <span style="left:0">Home</span>
    <span style="left:69px">About Us</span>
    <span style="left:139px">Success</span>
    <span style="left:214px">Stories</span>
    <span style="left:280px">FAQs</span>
    <span style="left:334px">Blog</span>
    <span style="left:372px">Login</span>
  </nav>
  <div class="social"><i></i><i></i><i></i><i></i><i></i></div>
</header>

<section class="hero">
  <h1>Marketing Site Creation, Made Easy...</h1>
  <p class="lead">Lorem Ipsum is simply dummy text of the printing and typesetting industry. Lorem Ipsum is simply dummy text of the .</p>
  <div class="hero-visual" role="img" aria-label="Laptop showing an analytics chart with a magnifying glass"></div>
  <ul class="feature-list">
    <li><svg viewBox="0 0 20 20"><circle cx="10" cy="10" r="8" fill="none" stroke="#333" stroke-width="2.5"/><circle cx="10" cy="10" r="3.5" fill="#333"/></svg>Create Sales Pages</li>
    <li><svg viewBox="0 0 20 20"><circle cx="10" cy="10" r="8" fill="none" stroke="#333" stroke-width="2.5"/><circle cx="10" cy="10" r="3.5" fill="#333"/></svg>Converting Landing Pages</li>
    <li><svg viewBox="0 0 20 20"><circle cx="10" cy="10" r="8" fill="none" stroke="#333" stroke-width="2.5"/><circle cx="10" cy="10" r="3.5" fill="#333"/></svg>Complete Launch Funnels</li>
    <li><svg viewBox="0 0 20 20"><circle cx="10" cy="10" r="8" fill="none" stroke="#333" stroke-width="2.5"/><circle cx="10" cy="10" r="3.5" fill="#333"/></svg>Authority Blog Sites</li>
  </ul>
  <div class="cta-button">Click Here to get<br>Pagewick Method</div>
</section>

<section class="stories">
  <article class="story" style="left:107px">
    <div class="story-video" role="img" aria-label="Video of a customer telling his success story"></div>
    <div style="margin-left:20px">
      <h3>Marcus T. (Success Story)</h3>
      <p>Lorem Ipsum is simply dummy text of the printing and typesetting industry.</p>
    </div>
  </article>
  <article class="story" style="left:459px">
    <div class="story-video alt" role="img" aria-label="Video of a customer telling his success story"></div>
    <div style="margin-left:20px;margin-top:-3px">
      <h3>Jonas. (Success Story)</h3>
      <p>Lorem Ipsum is simply dummy text of the printing and typesetting industry.</p>
    </div>
  </article>
</section>

<section class="create-band">
  <h2>What Can You Create With Pagewick Method</h2>
  <p>Lorem Ipsum is simply dummy text of the printing and typesetting industry.</p>
</section>

<section class="capabilities">
  <div class="capability" style="left:128px;top:38px">
    <div class="cap-icon blue"></div>
    <div><h4>Landing Pages</h4><p>Lorem Ipsum is simply dummy text of the printing</p></div>
  </div>
  <div class="capability" style="left:478px;top:38px">
    <div class="cap-icon amber"></div>
    <div><h4>Secure Membership Portals</h4><p>Lorem Ipsum is simply dummy text of the printing</p></div>
  </div>
  <div class="capability" style="left:128px;top:128px">
    <svg width="46" height="46" viewBox="0 0 46 46"><circle cx="18" cy="18" r="13" fill="none" stroke="#2b3440" stroke-width="4"/><path d="M27 27 L42 42" stroke="#2b3440" stroke-width="6" stroke-linecap="round"/></svg>
    <div><h4>Sales &amp; Marketing Pages</h4><p>Lorem Ipsum is simply dummy text of the printing</p></div>
  </div>
  <div class="capability" style="left:472px;top:128px">
    <svg width="48" height="42" viewBox="0 0 48 42"><path d="M2 4 H10 L16 28 H42 L46 10 H12" fill="none" stroke="#111" stroke-width="4" stroke-linejoin="round"/><circle cx="19" cy="36" r="4" fill="#111"/><circle cx="38" cy="36" r="4" fill="#111"/></svg>
    <div><h4>Product Launch Funnels</h4><p>Lorem Ipsum is simply dummy text of the printing</p></div>
  </div>
</section>

<section class="guarantee">
  <div class="guarantee-badge" role="img" aria-label="Satisfaction guarantee seal"></div>
  <h3>100% Money Back Guarantee</h3>
  <p>Lorem Ipsum is simply dummy text of the printing and typesetting industry. Lorem Ipsum has been the industry's standard dummy text ever since the 1500s, when an unknown printer took a galley of type and scrambled it to make a type specimen book. It has survived not only five centuries, but also the leap into electronic typesetting, remaining essentially unchanged. It was popularised in the 1960s with the release of Transfix sheets containing Lorem Ipsum passages, and more recently with desktop publishing software like Quillset Layout including versions of Lorem Ipsum.</p>
</section>

<section class="questions">
  <h3>STILL HAVE QUEATIONS?</h3>
  <svg width="34" height="36" viewBox="0 0 34 36"><path d="M12 20 V6 a3 3 0 0 1 6 0 V16 a3 3 0 0 1 6 0 V18 a3 3 0 0 1 6 0 V26 c0 5-4 8-9 8 h-4 c-4 0-6-2-8-5 l-5-7 a3 3 0 0 1 5-3 z" fill="none" stroke="#1f1f1f" stroke-width="2.2" stroke-linejoin="round"/></svg>
</section>

<footer class="site-footer">
  <span class="copy">Copyright © 2015 Pagewick Method · All Rights Reserved</span>
  <span class="legal"><span>Privacy Policy</span><span>Legal Information</span></span>
</footer>

</div>
</body>
</html>
```